"Sketch Onward Club" Social Art Website Design

I need a design for a website I am building, which will be called Sketch Onward Club. I have attached the selected logo for the site. The site will be about drawing/art, and how art can be used to brighten a stranger's day as a random act of kindness. In real life, people will receive a drawing or piece of art with details for this site on it. They will in turn be able to give a drawing or piece of art to someone else, thus building a 'chain' of people who are related to each other through the drawings they have received. This should create a strong 'social' aspect to the site. There will be areas of the site for seeing other drawings/art that have been submitted, as well as for seeing different statistics (how many drawings have been submitted, where, how people are connected, etc.).

Target Market(s)

No specific target market.

Industry/Entity Type

Building

Coding

Number of Pages Required

1 page

Font styles to use
Sans Serif
Decorative

Requirements
Must have
• Must use the logo supplied.
Nice to have
• Should be colourful and artistic. References to art tools should be primarily around drawing, though painting can also feature. Colour scheme to match the logo would be ideal.

```html
<!DOCTYPE html>
<html lang="en">
<head>
<meta charset="utf-8">
<title>Sketch Onward Club</title>
<link href="https://fonts.googleapis.com/css2?family=Open+Sans:wght@400;600;700&family=Chewy&display=swap" rel="stylesheet">
<style>
:root{
  --pink:#ee2a7b;
  --teal:#1eb4c8;
  --orange:#f6a623;
  --blue:#2b7bd3;
  --ink:#3b3b3b;
  --muted:#8a8a8a;
  --line:#e3e3e3;
  --paper:#ffffff;
  --soft:#f4f5f7;
}
*{box-sizing:border-box;margin:0;padding:0}
html,body{width:753px;height:1200px;overflow:hidden}
body{font-family:"Open Sans",Arial,sans-serif;color:var(--ink);background:var(--paper);position:relative}

.site-header{height:50px;display:flex;align-items:center;justify-content:space-between;padding:0 28px 0 30px;border-bottom:1px solid var(--line)}
.brand{display:flex;align-items:center;gap:7px;font-weight:700;font-size:13px;color:var(--pink)}
.brand-dot{width:14px;height:14px;border-radius:50%;background:var(--teal)}
.main-nav{display:flex;align-items:center;gap:17px;font-size:7.5px;font-weight:600;color:var(--pink);letter-spacing:.3px}
.main-nav .active{background:var(--pink);color:#fff;padding:5px 8px}
.login-btn{background:var(--teal);color:#fff;padding:6px 13px;border-radius:2px;margin-left:6px}

.hero{position:relative;height:300px;background:linear-gradient(100deg,#fff 55%,#f1f2f4 55%)}
.hero-copy{position:absolute;left:52px;top:112px}
.hero-copy .lead{font-size:24px;color:var(--ink);line-height:1.1}
.hero-copy h1{font-family:"Chewy",cursive;font-weight:400;font-size:30px;color:var(--teal);line-height:1.15;letter-spacing:.5px}
.hero-btn{display:inline-block;margin-top:12px;border:1px solid var(--teal);color:var(--teal);font-size:7.5px;padding:4px 9px;border-radius:2px}
.hero-art{position:absolute;left:380px;top:20px;width:345px;height:275px;background:radial-gradient(ellipse 55% 45% at 58% 45%,#fbe0ec 0%,#f6f0f3 45%,rgba(241,242,244,0) 75%),radial-gradient(ellipse 30% 20% at 85% 20%,#c8eef2,rgba(241,242,244,0) 80%),radial-gradient(ellipse 35% 18% at 35% 85%,#bfe9ef,rgba(241,242,244,0) 85%)}
.arrow{position:absolute;top:150px;width:18px;height:18px}
.arrow.left{left:10px}.arrow.right{right:10px}
.dots{position:absolute;left:52px;top:282px;display:flex;gap:4px}
.dots span{width:5px;height:5px;border-radius:50%;background:var(--line)}
.dots span:first-child{width:12px;border-radius:3px;background:var(--pink)}

.mission{height:240px;background:var(--pink);position:relative;color:#fff}
.mission-art{position:absolute;left:70px;top:0;width:170px;height:240px;background:radial-gradient(ellipse 40% 48% at 50% 50%,#fbe7d6 0%,#f7b9cf 55%,rgba(238,42,123,0) 100%)}
.mission-text{position:absolute;left:250px;top:30px;width:420px}
.mission-text h2{font-size:13px;font-weight:700;margin-bottom:6px}
.mission-text p{font-size:7.5px;line-height:1.6;margin-bottom:12px}

.artwork{padding-top:12px;height:238px;position:relative}
.section-title{text-align:center;font-size:13px;font-weight:700;color:#555}
.cards{display:flex;gap:17px;justify-content:center;margin-top:12px}
.card{width:218px;border:1px solid var(--line);background:#fff}
.card-img{height:108px}
.card-img.sunset{background:linear-gradient(180deg,#f39a1e,#c9501a 70%,#3a1d10)}
.card-img.sea{background:linear-gradient(180deg,#7fb8e4,#3b7bb5 55%,#d7e9f2)}
.card-img.lighthouse{background:linear-gradient(180deg,#e28a4e,#9c5a8c 55%,#3d5f7a)}
.card-body{text-align:center;padding:10px 0 6px}
.card-body h3{font-size:10px;font-weight:600;color:#555}
.card-body small{font-size:6.5px;color:var(--muted)}
.card-foot{border-top:1px solid var(--line);height:22px;display:flex;align-items:center;justify-content:center}
.artwork .arrow{top:130px}

.stats{height:190px;position:relative;background:var(--soft)}
.stat{position:absolute;left:56px;width:135px;height:58px;display:flex;align-items:center;gap:10px;padding-left:14px;color:#fff}
.stat.drawings{top:22px;background:var(--orange)}
.stat.received{top:98px;background:var(--blue)}
.stat b{display:block;font-size:21px;line-height:1}
.stat span{font-size:6.5px}
.world-map{position:absolute;left:425px;top:22px;width:300px;height:160px;background:radial-gradient(ellipse 50% 45% at 50% 50%,#d3d6db 0%,#e3e5e9 55%,rgba(244,245,247,0) 100%)}
.map-pin{position:absolute;left:560px;top:14px}

.contact{height:130px;text-align:center;padding-top:10px;position:relative}
.contact .section-title{font-size:14px;margin-bottom:10px}
.fields{display:flex;gap:12px;justify-content:center}
.field{width:206px;height:22px;border:1px solid var(--line);font-size:7px;color:var(--muted);text-align:left;padding:6px 8px}
.field.message{width:642px;height:30px;margin:8px auto 0}
.send-btn{position:absolute;left:366px;top:110px;width:22px;height:22px;border-radius:50%;background:var(--teal);display:flex;align-items:center;justify-content:center}

.site-footer{position:absolute;left:0;bottom:0;width:753px;height:40px;background:var(--pink);color:#fff;font-size:7px;padding:16px 0 0 14px}
.to-top{position:absolute;right:20px;top:-9px;width:18px;height:18px;border-radius:50%;background:var(--orange)}
</style>
</head>
<body>
<header class="site-header">
  <div class="brand"><span class="brand-dot"></span>Sketch Onward Club</div>
  <nav class="main-nav">
    <span class="active">HOME</span><span>FIND A DRAWING</span><span>ABOUT</span><span>FAQ</span><span>REPORT</span><span>OUR POLICIES</span><span>CONTACT</span>
    <span class="login-btn">LOG IN</span>
  </nav>
</header>

<section class="hero">
  <div class="hero-copy">
    <div class="lead">Welcome to</div>
    <h1>Sketch Onward Club</h1>
    <span class="hero-btn">Start Drawing</span>
  </div>
  <div class="hero-art" role="img" aria-label="Illustration of hands drawing a heart of flowers on paper with coloured pencils"></div>
  <svg class="arrow left" viewBox="0 0 18 18"><path d="M12 3 5 9l7 6" fill="none" stroke="#999" stroke-width="1.5"/></svg>
  <svg class="arrow right" viewBox="0 0 18 18"><path d="M6 3l7 6-7 6" fill="none" stroke="#999" stroke-width="1.5"/></svg>
  <div class="dots"><span></span><span></span><span></span></div>
</section>

<section class="mission">
  <div class="mission-art" role="img" aria-label="Cartoon child artist holding a paintbrush and palette"></div>
  <div class="mission-text">
    <h2>What we Believe</h2>
    <p>"We believe that the gift of a hand-drawn picture, a simple sketch with a kind message for a stranger, can brighten up someone's day and make the world just a little bit kinder. Every piece carries one request: pass it on, so that one drawing becomes a chain of people linked together by art."</p>
    <h2>About us</h2>
    <p>Sketch Onward Club began with one drawing left on a park bench. Today members share sketches, follow where their art travels next, and see how each small gift connects friends and strangers across the whole world, one page at a time, with colour and care.</p>
  </div>
</section>

<section class="artwork">
  <h2 class="section-title">Recently Submited Artwork</h2>
  <div class="cards">
    <article class="card"><div class="card-img sunset" role="img" aria-label="Painting of a sunset with palm trees"></div><div class="card-body"><h3>Art Title</h3><small>by Artist Name</small></div><div class="card-foot"><svg width="10" height="10" viewBox="0 0 10 10"><path d="M5 9 1.5 5.5A2.2 2.2 0 0 1 5 2.8a2.2 2.2 0 0 1 3.5 2.7z" fill="none" stroke="#bbb"/></svg></div></article>
    <article class="card"><div class="card-img sea" role="img" aria-label="Painting of waves and seagulls"></div><div class="card-body"><h3>Art Title</h3><small>by Artist Name</small></div><div class="card-foot"><svg width="10" height="10" viewBox="0 0 10 10"><path d="M5 9 1.5 5.5A2.2 2.2 0 0 1 5 2.8a2.2 2.2 0 0 1 3.5 2.7z" fill="none" stroke="#bbb"/></svg></div></article>
    <article class="card"><div class="card-img lighthouse" role="img" aria-label="Painting of a lighthouse on a rocky coast"></div><div class="card-body"><h3>Art Title</h3><small>by Artist Name</small></div><div class="card-foot"><svg width="10" height="10" viewBox="0 0 10 10"><path d="M5 9 1.5 5.5A2.2 2.2 0 0 1 5 2.8a2.2 2.2 0 0 1 3.5 2.7z" fill="none" stroke="#bbb"/></svg></div></article>
  </div>
  <svg class="arrow left" viewBox="0 0 18 18"><path d="M12 3 5 9l7 6" fill="none" stroke="#999" stroke-width="1.5"/></svg>
  <svg class="arrow right" viewBox="0 0 18 18"><path d="M6 3l7 6-7 6" fill="none" stroke="#999" stroke-width="1.5"/></svg>
</section>

<section class="stats">
  <div class="stat drawings">
    <svg width="26" height="22" viewBox="0 0 26 22"><circle cx="13" cy="6" r="4.5" fill="#fff"/><path d="M4 21c0-5 4-8 9-8s9 3 9 8z" fill="#fff"/><circle cx="4.5" cy="8" r="3" fill="#fff" opacity=".8"/><circle cx="21.5" cy="8" r="3" fill="#fff" opacity=".8"/></svg>
    <div><b>1.5K</b><span>Drawings Submitted</span></div>
  </div>
  <div class="stat received">
    <svg width="26" height="22" viewBox="0 0 26 22"><rect x="2" y="3" width="17" height="15" fill="none" stroke="#fff" stroke-width="2"/><path d="M5 15l4-5 3 3 2-2 3 4z" fill="#fff"/><path d="M16 19 24 6l2 1.2-8 13z" fill="#fff"/></svg>
    <div><b>1.7K</b><span>Drawings Received</span></div>
  </div>
  <div class="world-map" role="img" aria-label="Dotted world map showing where drawings were shared"></div>
  <svg class="map-pin" width="20" height="26" viewBox="0 0 20 26"><path d="M10 1a8 8 0 0 0-8 8c0 6 8 16 8 16s8-10 8-16a8 8 0 0 0-8-8z" fill="#ee2a7b"/><circle cx="10" cy="9" r="3.5" fill="#f6a623"/></svg>
</section>

<section class="contact">
  <h2 class="section-title">Contact us</h2>
  <div class="fields">
    <div class="field">Full name...</div><div class="field">Email address...</div><div class="field">Subject...</div>
  </div>
  <div class="field message">Type your message here...</div>
  <span class="send-btn"><svg width="10" height="10" viewBox="0 0 10 10"><path d="M1 5 9 1 6 9 5 6z" fill="#fff"/></svg></span>
</section>

<footer class="site-footer">© 2016 Sketch Onward Club<span class="to-top"></span></footer>
</body>
</html>
```